Private label Bottled water label design

We are launching private label water bottle case packs with our brand “tallybrook”
Need bottle labels design as well as case pack design artwork. Bottle is 16.9oz similar to pet quarvin plimsey bottles.
It will be spring water.
Case pack will be of 24 bottles
Tallybrook is a chain of convenience stores in Texas
www.tallybrookmarts.example
I have attached pictures of quarvin water. It would be similar packaging for single and case pack.

Target Market(s)

Male female shoppers middle aged. Take home package or single serve in cold vault

Industry/Entity Type

Water bottle retail

Colors
0054AA
0677BA
7BADD7
CADEEF
E8F1F8
59FF00
82FF00
B8FF75
E3FFCB
F4FFEA

Requirements
Must have
• Very premium look. Use the logo of tallybrook
Nice to have
• Elegant premium water look
Should not have
• I am open to all

```html
<!DOCTYPE html>
<html lang="en">
<head>
<meta charset="UTF-8">
<title>Tallybrook Natural Spring Water – Bottle Label</title>
<link rel="stylesheet" href="https://fonts.googleapis.com/css2?family=Open+Sans:wght@400;700;800&family=Nunito:wght@900&family=Quicksand:wght@500&display=swap">
<style>
  :root {
    --page-bg: #eeeff2;
    --blue-deep: #0677ba;
    --blue-bright: #1a8fe8;
    --blue-mid: #7badd7;
    --blue-pale: #cadeef;
    --blue-mist: #e8f1f8;
    --green-label: #8fd11c;
    --green-pill: #8ccc16;
    --ink: #0d1a26;
    --ink-soft: #1f2f3d;
  }
  * { margin: 0; padding: 0; box-sizing: border-box; }
  html, body {
    width: 1200px;
    height: 1200px;
    overflow: hidden;
    background: var(--page-bg);
  }
  .canvas {
    position: relative;
    width: 1200px;
    height: 1200px;
  }
  .wrap-label {
    position: absolute;
    left: 48px;
    top: 510px;
    width: 1113px;
    height: 181px;
    overflow: hidden;
    background:
      linear-gradient(180deg, rgba(255,255,255,0) 0%, rgba(202,222,239,0.55) 38%, rgba(255,255,255,0) 70%),
      linear-gradient(90deg, #2a88d8 0%, #4ea3e0 18%, #5aa9e2 40%, #1a8fe8 62%, #2b95ea 85%, #5db5e6 100%);
  }
  .wrap-label::after {
    content: "";
    position: absolute;
    inset: 0;
    background: linear-gradient(180deg, rgba(6,119,186,0.25) 0%, rgba(255,255,255,0) 35%, rgba(6,119,186,0) 70%, rgba(6,119,186,0.35) 100%);
    pointer-events: none;
  }
  .burst-art {
    position: absolute;
    left: 336px;
    top: -30px;
    width: 440px;
    height: 240px;
    background: radial-gradient(ellipse at 50% 50%, rgba(255,255,255,0.95) 0%, rgba(232,241,248,0.75) 18%, rgba(123,173,215,0.35) 45%, rgba(123,173,215,0) 72%);
    z-index: 1;
  }
  .brand-panel {
    position: absolute;
    inset: 0;
    z-index: 2;
  }
  .brand-name {
    position: absolute;
    left: 0;
    width: 100%;
    top: 50px;
    text-align: center;
    font-family: "Open Sans", sans-serif;
    font-weight: 800;
    font-size: 40px;
    letter-spacing: -1px;
    color: var(--ink);
    line-height: 1;
  }
  .brand-dot {
    display: inline-block;
    width: 12px;
    height: 12px;
    margin-left: 6px;
    margin-top: 2px;
    border-radius: 50%;
    background: var(--green-label);
    vertical-align: top;
  }
  .product-name {
    position: absolute;
    left: 0;
    width: 100%;
    top: 108px;
    text-align: center;
    font-family: "Nunito", sans-serif;
    font-weight: 900;
    font-size: 21px;
    color: var(--green-label);
    line-height: 1;
  }
  .tagline-pill {
    position: absolute;
    left: 480px;
    top: 138px;
    width: 152px;
    height: 19px;
    border-radius: 10px;
    background: var(--green-pill);
    font-family: "Quicksand", sans-serif;
    font-weight: 500;
    font-size: 12.5px;
    color: var(--ink-soft);
    text-align: center;
    line-height: 19px;
  }
  .content-note {
    position: absolute;
    left: 0;
    width: 100%;
    top: 163px;
    text-align: center;
    font-family: "Open Sans", sans-serif;
    font-weight: 700;
    font-size: 8px;
    line-height: 11px;
    color: var(--ink);
  }
  .storage-note {
    position: absolute;
    left: 28px;
    top: 152px;
    font-family: "Quicksand", sans-serif;
    font-weight: 500;
    font-size: 9.5px;
    line-height: 12px;
    white-space: nowrap;
    color: var(--ink-soft);
    z-index: 2;
  }
  .info-block {
    position: absolute;
    left: 928px;
    top: 41px;
    font-family: "Open Sans", sans-serif;
    font-size: 9px;
    line-height: 11.2px;
    white-space: nowrap;
    color: var(--ink);
    z-index: 2;
  }
  .info-block h3 {
    font-size: 9px;
    font-weight: 700;
  }
  .info-block p + h3 { margin-top: 11px; }
</style>
</head>
<body>
  <main class="canvas">
    <section class="wrap-label">
      <div class="burst-art" role="img" aria-label="Radiating light burst with water splash behind the brand name"></div>

      <div class="brand-panel">
        <div class="brand-name">tallybrook<span class="brand-dot"></span></div>
        <div class="product-name">Natural Spring Water</div>
        <div class="tagline-pill">Pure and Refreshing</div>
        <div class="content-note">100% Natural Spring Water</div>
      </div>

      <p class="storage-note">Store in a cool, dry place away from direct sunlight.</p>

      <div class="info-block">
        <h3>Environmental Responsibility:</h3>
        <p>We are committed to sustainability.<br>Please recycle this bottle.</p>
        <h3>Disclaimer:</h3>
        <p>This information is for reference<br>purposes only. It is recommended<br>to check the label on the actual<br>product for the most accurate<br>information.</p>
      </div>
    </section>
  </main>
</body>
</html>
```